Simplified minimalist but bold website

Design a website for a brand 'Brighten Each Morning' that shares ideas to make managing home and health easier through email swap series, webinars and eventually courses.

Simple landing page to attract users to sign up for a freebie.

Target Market(s)

women with families & homes to run

Number of Pages Required

1 page

Font styles to use
Sans Serif

Colors
e667a6
b768aa
acd136
ffffff
959595

Requirements
Must have
• Simplified look, line icons, opt-in template, contact us form

```html
<!DOCTYPE html>
<html lang="en">
<head>
<meta charset="utf-8">
<title>Brighten Each Morning</title>
<link href="https://fonts.googleapis.com/css2?family=Ubuntu:ital,wght@0,300;0,400;0,500;0,700;1,400&display=swap" rel="stylesheet">
<style>
:root{
  --pink:#e667a6;
  --purple:#b768aa;
  --green:#acd136;
  --blue:#2f9bd6;
  --white:#ffffff;
  --grey:#959595;
  --ink:#1c1c1c;
  --field:#f2f2f2;
  --footer:#232323;
  --footer-deep:#141414;
}
*{margin:0;padding:0;box-sizing:border-box}
html,body{width:777px;height:1200px;overflow:hidden}
body{font-family:'Ubuntu',sans-serif;color:var(--ink);background:var(--white);position:relative}
.btn{position:absolute;display:flex;align-items:center;justify-content:center;height:25px;border-radius:3px;background:var(--green);color:var(--white);font-weight:700;font-size:9px;letter-spacing:2.2px;text-transform:uppercase}
.btn--blue{background:var(--blue)}

/* hero */
.hero{position:absolute;left:0;top:0;width:777px;height:369px;overflow:hidden}
.hero__photo{position:absolute;inset:0;background:linear-gradient(120deg,#e64f9b 0%,#c24a9c 45%,#a4479a 75%,#c46ab2 100%)}
.hero__title{position:absolute;top:122px;width:100%;text-align:center;color:var(--white);font-weight:700;font-size:36px;letter-spacing:.3px}
.hero__sub{position:absolute;top:173px;width:100%;text-align:center;color:var(--white);font-size:15px;font-weight:400}
.hero .btn{left:338px;top:207px;width:102px}
.hero__dots{position:absolute;top:335px;left:368px;display:flex;gap:7px}
.hero__dots span{width:5px;height:5px;border-radius:50%;background:var(--white)}
.hero__dots span.is-active{background:#3a3aa0}

/* offers */
.offer{position:absolute;top:369px;width:388px;height:412px;text-align:center}
.offer--left{left:37px}
.offer--right{left:357px}
.offer__tag{position:absolute;width:100%;font-style:italic;font-size:13px}
.offer__title{position:absolute;width:100%;top:81px;font-weight:700;font-size:13px;letter-spacing:.3px}
.offer__text{position:absolute;width:100%;top:113px;font-size:8.6px;line-height:10.5px}
.field{position:absolute;width:231px;height:25px;border-radius:4px;background:var(--field);display:flex;align-items:center;justify-content:center;font-style:italic;font-size:8.5px;color:#333}
.guide-art{position:absolute;left:109px;top:117px;width:171px;height:103px;border-radius:3px;background:linear-gradient(90deg,var(--purple) 0%,var(--purple) 48%,var(--pink) 52%,var(--pink) 100%)}

/* series */
.series{position:absolute;top:781px;left:0;width:777px;height:343px;overflow:hidden;text-align:center}
.series__photo{position:absolute;inset:0;background:linear-gradient(90deg,#e6e4df 0%,#f2f1ee 40%,#dcdad5 70%,#ecebe6 100%)}
.series__title{position:absolute;top:57px;width:100%;font-weight:700;font-size:19px}
.series__text{position:absolute;top:105px;width:100%;font-size:8.6px;line-height:10.7px}
.series__text p{margin-bottom:10px}
.series .btn{left:318px;top:248px;width:141px}

/* footer */
.footer{position:absolute;top:1124px;left:0;width:777px;height:43px;background:var(--footer);display:flex;justify-content:center;align-items:center;gap:14px}
.social{display:flex;align-items:center;gap:4px;color:var(--grey);font-size:7px;letter-spacing:.3px}
.social__dot{width:9px;height:9px;border:1px solid var(--grey);border-radius:50%}
.legal{position:absolute;top:1167px;left:0;width:777px;height:33px;background:var(--footer-deep);color:#cfcfcf;font-size:6.5px;letter-spacing:.3px;display:flex;align-items:center;justify-content:center}
</style>
</head>
<body>

<header class="hero">
  <div class="hero__photo" role="img" aria-label="Photo of a young couple relaxing at home with a tablet, tinted pink"></div>
  <h1 class="hero__title">Brighten Each Morning.</h1>
  <p class="hero__sub">Chances are life is a little overwhelming.</p>
  <a class="btn">Let us help</a>
  <div class="hero__dots"><span></span><span class="is-active"></span><span></span><span></span></div>
</header>

<section class="offer offer--left">
  <p class="offer__tag" style="top:47px">Baby Steps... (try out a few of our tricks)</p>
  <h2 class="offer__title">SWAPS EMAIL SERIES</h2>
  <div class="offer__text">
    <p>Save TIME, MONEY and SANITY with simple product swaps.</p>
    <p style="margin-top:11px">Reduce the amount of work it takes to run your home.<br>Swap out existing products for more sustainable ones.<br>Each swap saves you work, clutter, time &amp; money.</p>
  </div>
  <a class="btn" style="left:79px;top:186px;width:128px">See sample swap</a>
  <a class="btn btn--blue" style="left:218px;top:186px;width:91px">Learn more</a>
  <p class="offer__tag" style="top:231px">Send your ideas my way...</p>
  <div class="field" style="left:75px;top:260px">Name</div>
  <div class="field" style="left:75px;top:294px">Email</div>
  <a class="btn" style="left:124px;top:330px;width:141px">Send me the guide!</a>
</section>

<section class="offer offer--right">
  <p class="offer__tag" style="top:53px">Big Leap... (I'm ready to roll up my sleeves)</p>
  <h2 class="offer__title">DECLUTTERING GUIDE</h2>
  <div class="guide-art" role="img" aria-label="Illustration of two tilted guide cards, purple and pink"></div>
  <div class="field" style="left:79px;top:260px">Name</div>
  <div class="field" style="left:79px;top:294px">Email</div>
  <a class="btn" style="left:124px;top:330px;width:141px">Sign me up!</a>
</section>

<section class="series">
  <div class="series__photo" role="img" aria-label="Faded photo of a consultant meeting an older couple in a bright living room"></div>
  <h2 class="series__title">Swaps Email Series</h2>
  <div class="series__text">
    <p>Save TIME, MONEY and SANITY with simple product swaps.<br>And reduce the amount of work it takes to run your home.<br>Swap out existing products for more sustainable ones.<br>Each swap save you work, clutter, time &amp; money.</p>
    <p>You get an email 2x weekly for 6-12 weeks only<br>Get even more if you feel they are helpful to you</p>
    <p>Join our monthly SIMPLE SWAP SHARING web jams with other mums and get even more ideas.</p>
    <p>Better yet, come with great tips of your own to share.</p>
  </div>
  <a class="btn">Sign me up!</a>
</section>

<footer class="footer">
  <span class="social"><span class="social__dot"></span>Nook</span>
  <span class="social"><span class="social__dot"></span>Chime</span>
  <span class="social"><span class="social__dot"></span>Orbit</span>
  <span class="social"><span class="social__dot"></span>Drift</span>
  <span class="social"><span class="social__dot"></span>Vista</span>
</footer>
<div class="legal">© COPYRIGHTS 2018 &nbsp;|&nbsp; WWW.BRIGHTENMORNING.COM</div>

</body>
</html>
```